Redesign two existing website pages and one new landing page for dental office

I need to redesign two webpages on my dental website, the Home page (http://brelvoortdental.com) and the Dental Implant Services page (http://www.brelvoortdental.com/dental-implant-services) and also create a landing page for the Dental Implant Services page.

Please use the same color scheme, slogans and subtitles for the redesign pages and create a reserved video spot on each page. The video spots should not be too big but not too small either and positioned in a central key location on each of the pages. The final redesigned pages should communicate leadership, confidence and trust.

The new landing page for the Dental implant Services page must not have any hyperlinks on the page and must entice the viewer to give name and email before downloading a "Free" eBook called "Is a Fresh Smile Worth Waiting For?" Any added photo images to this new page must be smiling.
Updates

Project Deadline Extended Reason: I got feedback that my project was not long enough so I'm extending it by 5 days. Added Thursday, April 16, 2015

Target Market(s)

People who are middle-age to seniors.

Industry/Entity Type

Dental

Coding

Coded - Design and coding required

Number of Pages Required

3 page

Requirements
Must have
• Compatible with existing website colors and theme.

```html
<!DOCTYPE html>
<html lang="en">
<head>
<meta charset="utf-8">
<title>Brelvoort Dental Care – Hygiene Services</title>
<link rel="stylesheet" href="https://fonts.googleapis.com/css2?family=Noto+Sans:wght@300;400;600&display=swap">
<style>
  :root {
    --teal: #336766;
    --teal-text: #2f6563;
    --band-grey: #cfd1d1;
    --ring-grey: #d2d2d2;
    --white: #ffffff;
    --photo-warm-a: #f3d9c8;
    --photo-warm-b: #c99a7c;
    --photo-clinic-a: #e9f1f2;
    --photo-clinic-b: #4b9a95;
  }
  * { margin: 0; padding: 0; box-sizing: border-box; }
  html, body { width: 1200px; height: 900px; overflow: hidden; background: var(--white); }
  body { font-family: "Noto Sans", sans-serif; color: var(--teal-text); position: relative; }

  .service-photo {
    position: absolute; left: 63px; width: 192px; height: 192px;
    border-radius: 50%; border: 3px solid var(--ring-grey);
  }
  .service-photo--dentures { top: -34px; background: radial-gradient(circle at 45% 40%, var(--photo-warm-a), var(--photo-warm-b)); }
  .service-photo--sedation { top: 238px; background: radial-gradient(circle at 55% 50%, var(--photo-clinic-a), var(--photo-clinic-b)); }
  .service-label { position: absolute; width: 220px; left: 49px; text-align: center; font-size: 20px; font-weight: 600; }
  .service-label--dentures { top: 168px; }
  .service-label--sedation { top: 437px; }

  .tips { position: absolute; left: 330px; top: 2px; font-size: 16.5px; line-height: 20.8px; }
  .divider { position: absolute; left: 331px; top: 98px; width: 811px; height: 2px; background: var(--teal); }
  .section-title { position: absolute; left: 326px; top: 133px; font-size: 29px; font-weight: 400; }
  .intro { position: absolute; left: 331px; top: 188px; font-size: 16.5px; }
  .hygiene-list { position: absolute; left: 331px; top: 230px; list-style: none; font-size: 16.5px; line-height: 20.9px; }

  .band { position: absolute; left: 0; width: 1200px; height: 12px; background: var(--band-grey); }
  .band--top { top: 500px; }
  .band--bottom { top: 834px; }
  .site-footer { position: absolute; left: 0; top: 512px; width: 1200px; height: 322px; background: var(--teal); color: var(--white); }
  .footer-col { position: absolute; top: 43px; }
  .footer-col h2 { font-size: 20px; font-weight: 400; margin-bottom: 13px; }
  .footer-col ul { list-style: none; }
  .col-blog { left: 48px; width: 270px; }
  .col-blog ul { margin-left: 2px; font-size: 17px; font-weight: 300; line-height: 29px; }
  .col-services { left: 376px; }
  .col-services ul { margin-left: 1px; font-size: 17px; font-weight: 300; line-height: 29px; }
  .col-nav { left: 620px; }
  .col-nav ul { margin-left: 8px; margin-top: 18px; font-size: 17.5px; line-height: 35px; }
  .col-contact { left: 892px; width: 270px; }
  .col-contact p.lead { font-size: 17px; font-weight: 300; line-height: 23px; margin-top: -1px; }
  .col-contact strong { font-weight: 600; }
  .contact-line { font-size: 17px; margin-left: 2px; line-height: 28px; }
  .contact-line--first { margin-top: 14px; }
  .contact-line--phone { font-weight: 600; }
  .contact-line--directions { margin-top: 8px; }

  .copyright { position: absolute; top: 858px; width: 1200px; text-align: center; padding-right: 90px; font-size: 17px; color: var(--teal-text); }
</style>
</head>
<body>
  <div class="service-photo service-photo--dentures" role="img" aria-label="Photo of a smiling senior couple"></div>
  <p class="service-label service-label--dentures">Beautiful Dentures</p>
  <div class="service-photo service-photo--sedation" role="img" aria-label="Photo of a dentist treating a relaxed patient"></div>
  <p class="service-label service-label--sedation">Sedation Dentistry</p>

  <ul class="tips" style="list-style:none">
    <li>Use dental floss at least once a day every day</li>
    <li>Limit sweetened foods and beverages to meal times</li>
    <li>Tobacco products are harmful to teeth and gums so don’t use them</li>
  </ul>
  <div class="divider"></div>

  <h1 class="section-title">Our Hygiene Services</h1>
  <p class="intro">Dental hygiene services we provide are:</p>
  <ul class="hygiene-list">
    <li>Dental Radiographs</li>
    <li>Dental Charting</li>
    <li>Dental Hygiene Therapy</li>
    <li>Dental, Periodontal and Oral Cancer Examinations</li>
    <li>Diagnosis and Treatment Planning of Dental Diseases</li>
    <li>Preventive Oral Health Management and Patient Education</li>
    <li>Cavity (Caries) Risk Assessment and Management</li>
    <li>Fluoride Therapy</li>
    <li>Soft Tissue Management (Gum Therapy)</li>
    <li>Supportive Periodontal Therapy</li>
    <li>Occlusal Sealants</li>
  </ul>

  <div class="band band--top"></div>
  <footer class="site-footer">
    <section class="footer-col col-blog">
      <h2>Recent Blog Posts</h2>
      <ul>
        <li>Conscious Sedation: A Way to Deal with Anxiety at the Dentist’s Office</li>
        <li>Pediatric Dentists and Their Im-portance in Today’s World</li>
        <li>Tooth Implant Facts</li>
        <li>Is Sedation Dentistry Cost Af-</li>
      </ul>
    </section>
    <section class="footer-col col-services">
      <h2>Services</h2>
      <ul>
        <li>Beautiful Dentures</li>
        <li>Cosmetic Denistr</li>
        <li>Dental Implant</li>
        <li>Sedation Denistry</li>
      </ul>
    </section>
    <nav class="footer-col col-nav">
      <h2>Navigation</h2>
      <ul>
        <li>Home</li>
        <li>About Us</li>
        <li>Dental Services</li>
        <li>Blog</li>
        <li>Contact Us</li>
        <li>Testimonials</li>
      </ul>
    </nav>
    <section class="footer-col col-contact">
      <h2>Contact Us</h2>
      <p class="lead">for all your general and cosmetic dental treatment and ask how to eliminate your dental pain and anxiety with <strong>sedation dentistry.</strong></p>
      <p class="contact-line contact-line--first">Email:&nbsp;&nbsp; info@brelvoortdental.com</p>
      <p class="contact-line contact-line--phone">Phone:&nbsp; (555) 014-2278</p>
      <p class="contact-line contact-line--directions">Directions</p>
    </section>
  </footer>
  <div class="band band--bottom"></div>
  <p class="copyright">©2014 Brelvoort Dental Care,</p>
</body>
</html>
```